Portrait of a Graduate

Our school community has created a document which describes the characteristics that every student who graduates from our school should possess. We would like a visual graphic to present the information to parents\ community. We came up with three buckets (Personal, Social, and Academic) and the concept "BLH Graduates Will Be Okay" is the central theme.
We are open to 2 different concepts:
1. A ven diagram of sorts, where the three buckets are each in an area - and the over lap is "BLH Graduates Will Be Okay"
2. Our logo has a sassafras leaf in it - using the leaves to represent each bucket and the central concept as the stem - or some other creative version.

The text to be used is below:

BLH Graduates Will Be Okay (at the center/on the stem)

1. Personal
They will:
have self-worth
advocate for themselves
feel secure in their future

2. Social
They will:
embrace differences
engage in trusting relationships
be compassionate (members of their community)

3. Academic
They will:
apply skills and strategies
creatively problem-solve
achieve individual success

```html
<!DOCTYPE html>
<html lang="en">
<head>
<meta charset="utf-8">
<title>Portrait of a Graduate</title>
<link href="https://fonts.googleapis.com/css2?family=Lora:wght@400;500;600;700&display=swap" rel="stylesheet">
<style>
  :root {
    --page-bg: #e9e9e9;
    --sheet: #ffffff;
    --navy: #1b2f4d;
    --navy-light: #2a4a78;
    --green: #2f6a33;
    --green-dark: #1f4a24;
    --orange: #f07a22;
    --orange-light: #f6995a;
    --gold: #f6c02e;
    --accent: #ee7420;
    --text: #444a52;
    --rule: #777b80;
    --swoosh: #f1f2f4;
  }
  * { margin: 0; padding: 0; box-sizing: border-box; }
  html, body { width: 1200px; height: 900px; overflow: hidden; }
  body { background: var(--page-bg); font-family: "Lora", Georgia, serif; position: relative; }

  .poster {
    position: absolute; left: 298px; top: 18px;
    width: 603px; height: 865px;
    background: var(--sheet);
    box-shadow: 0 2px 10px rgba(0,0,0,.12);
  }
  .poster__art { position: absolute; inset: 0; }

  .school-name {
    position: absolute; left: 0; right: 0; top: 66px;
    text-align: center; color: var(--navy);
    font-weight: 500; font-size: 26px; line-height: 1.15; letter-spacing: .5px;
  }
  .school-name__dot {
    display: inline-block; width: 12px; height: 12px; border-radius: 50%;
    background: var(--navy); margin-right: 8px; vertical-align: middle;
  }

  .pillar { position: absolute; color: var(--text); font-size: 13.5px; line-height: 16.6px; font-weight: 500; }
  .pillar__title { color: var(--accent); font-size: 23px; font-weight: 600; line-height: 28px; }
  .pillar__list { list-style: none; }
  .pillar__list li { padding-left: 10px; text-indent: -10px; }
  .pillar__list li::before { content: "» "; }
  .pillar--personal { left: 212px; top: 152px; }
  .pillar--social { left: 47px; top: 601px; width: 230px; }
  .pillar--academic { left: 375px; top: 596px; }

  .tagline {
    position: absolute; left: 0; right: 0; top: 742px;
    text-align: center; color: var(--accent);
    font-weight: 700; font-size: 38px; line-height: 40px;
  }
</style>
</head>
<body>
<main class="poster">
  <svg class="poster__art" width="603" height="865" viewBox="0 0 603 865" aria-hidden="true">
    <defs>
      <linearGradient id="grad-personal" x1="0" y1="0" x2="1" y2="1">
        <stop offset="0" stop-color="var(--navy)"/><stop offset="1" stop-color="var(--navy-light)"/>
      </linearGradient>
      <linearGradient id="grad-social" x1="0" y1="0" x2="1" y2="1">
        <stop offset="0" stop-color="var(--green)"/><stop offset="1" stop-color="var(--green-dark)"/>
      </linearGradient>
      <linearGradient id="grad-academic" x1="0" y1="1" x2="1" y2="0">
        <stop offset="0" stop-color="var(--orange-light)"/><stop offset="1" stop-color="var(--orange)"/>
      </linearGradient>
      <clipPath id="clip-personal"><circle cx="301" cy="381" r="79"/></clipPath>
      <clipPath id="clip-social"><circle cx="262" cy="463" r="80"/></clipPath>
    </defs>

    <path class="swoosh" d="M180 15 C 20 200, 20 520, 560 849 L 583 849 C 120 560, 60 260, 230 15 Z" fill="var(--swoosh)"/>
    <path class="swoosh" d="M40 15 C -10 300, 120 600, 460 849 L 500 849 C 160 600, 30 330, 90 15 Z" fill="#f6f7f8"/>

    <rect class="frame" x="18" y="15" width="565" height="834" fill="none" stroke="var(--navy)" stroke-width="3"/>
    <rect class="frame-inner" x="23" y="20" width="555" height="824" fill="none" stroke="#c9ccd1" stroke-width="1"/>

    <g class="connectors" stroke="var(--rule)" fill="none">
      <line x1="212" y1="249" x2="390" y2="249" stroke-width="3"/>
      <line x1="47" y1="591" x2="139" y2="591" stroke-width="3"/>
      <line x1="375" y1="591" x2="507" y2="591" stroke-width="3"/>
      <path d="M301 249 V333" stroke-width="1" stroke-dasharray="2 2"/>
      <path d="M86 591 V462 H238" stroke-width="1" stroke-dasharray="2 2"/>
      <path d="M437 591 V462 H358" stroke-width="1" stroke-dasharray="2 2"/>
    </g>

    <g class="venn">
      <circle cx="301" cy="381" r="79" fill="url(#grad-personal)"/>
      <circle cx="262" cy="463" r="80" fill="url(#grad-social)"/>
      <circle cx="340" cy="464" r="80" fill="url(#grad-academic)"/>
      <g clip-path="url(#clip-personal)">
        <circle cx="262" cy="463" r="80" fill="url(#grad-social)" clip-path="url(#clip-personal)"/>
        <circle cx="340" cy="464" r="80" fill="var(--gold)" clip-path="url(#clip-social)"/>
      </g>
      <circle cx="301" cy="333" r="3.5" fill="#8a8f96"/>
      <circle cx="238" cy="462" r="3.5" fill="#8a8f96"/>
      <circle cx="358" cy="462" r="3.5" fill="#8a8f96"/>
    </g>
  </svg>

  <div class="school-name"><span class="school-name__dot"></span>Brookline Hall School</div>

  <section class="pillar pillar--personal">
    <h2 class="pillar__title">1. Personal</h2>
    <p>They will:</p>
    <ul class="pillar__list">
      <li>have self-worth</li>
      <li>advocate for themselves</li>
      <li>feel secure in their future</li>
    </ul>
  </section>

  <section class="pillar pillar--social">
    <h2 class="pillar__title">2. Social</h2>
    <p>They will:</p>
    <ul class="pillar__list">
      <li>embrace differences</li>
      <li>engage in trusting relationships</li>
      <li>be compassionate (members of their community</li>
    </ul>
  </section>

  <section class="pillar pillar--academic">
    <h2 class="pillar__title">3. Academic</h2>
    <p>They will:</p>
    <ul class="pillar__list">
      <li>apply skills and strategies</li>
      <li>creatively problem-solve</li>
      <li>achieve individual success</li>
    </ul>
  </section>

  <h1 class="tagline">BLH Graduates<br>Will Be Okay</h1>
</main>
</body>
</html>
```